Consulting Company needs business card design

We need a business card design for a new consulting and business solutions company based in Bermuda called Corvane Holdings Limited. Looking for a double sided business card with one side only including the company logo thats attached and the other including contact information. Logo contains blue and turquoise colors and is fine to be on both sides of the card.
Contact Information for Business Card
Corvane Holdings Limited
P.O. Box KR318
Pemberly KR LT
Bermuda
Name: Marcus Telford
Position: Director
Telephone: 1 441 732 4590
Email: mtelford@corvane.bm
Website: www.corvane.bm

```html
<!DOCTYPE html>
<html lang="en">
<head>
<meta charset="utf-8">
<title>Corvane Holdings Limited – Business Card</title>
<link href="https://fonts.googleapis.com/css2?family=Lato:wght@400;700;900&display=swap" rel="stylesheet">
<style>
  :root {
    --bg: #2a2a2a;
    --blue: #29a3df;
    --blue-light: #34b4ea;
    --blue-dark: #1d8fcc;
    --teal: #1fb3a6;
    --white: #ffffff;
    --paper: #f4f4f4;
    --ink: #1e1e1e;
  }
  * { margin: 0; padding: 0; box-sizing: border-box; }
  html, body {
    width: 1200px; height: 997px; overflow: hidden;
    background: var(--bg);
    font-family: "Lato", sans-serif;
  }
  .card {
    position: absolute; left: 220px;
    width: 760px; height: 434px;
    overflow: hidden; border-radius: 4px;
  }
  .card--front { top: 50px; background: radial-gradient(ellipse at 60% 40%, var(--blue-light), var(--blue-dark)); }
  .card--back { top: 513px; background: var(--paper); }

  .tab { position: absolute; width: 60px; height: 180px; border-radius: 22px; }
  .tab--top-right { right: -22px; top: -22px; }
  .tab--bottom-left { left: -22px; bottom: -22px; height: 200px; }
  .card--front .tab { background: var(--white); }
  .card--back .tab { background: var(--blue); }

  .wordmark {
    position: absolute; left: 0; right: 0; text-align: center;
    font-weight: 900; letter-spacing: 2px; text-transform: uppercase;
    display: flex; align-items: center; justify-content: center; gap: 16px;
  }
  .wordmark__dot { width: 44px; height: 44px; border-radius: 50%; }
  .card--front .wordmark { top: 150px; font-size: 44px; color: var(--white); }
  .card--front .wordmark__dot { background: var(--white); width: 60px; height: 60px; }
  .card--back .wordmark { top: 40px; font-size: 30px; color: var(--blue); }
  .card--back .wordmark__dot { background: var(--blue); }

  .website {
    position: absolute; top: 340px; left: 0; right: 0; text-align: center;
    color: var(--white); font-size: 16px; letter-spacing: 6px; font-weight: 700;
  }

  .person { position: absolute; left: 150px; top: 170px; text-align: right; width: 230px; }
  .person__name { color: var(--blue); font-weight: 900; font-size: 22px; text-transform: uppercase; }
  .person__role { color: var(--ink); font-size: 15px; margin-top: 2px; }

  .contacts { position: absolute; left: 430px; top: 140px; list-style: none; }
  .contacts li { display: flex; align-items: center; gap: 12px; font-size: 17px; color: var(--ink); margin-bottom: 14px; }
  .contacts svg { width: 28px; height: 28px; flex: none; }

  .company { position: absolute; left: 0; right: 0; top: 290px; text-align: center; }
  .company__name { color: var(--blue); font-weight: 900; font-size: 24px; text-transform: uppercase; }
  .company__address { color: var(--ink); font-weight: 900; font-size: 19px; margin-top: 8px; }
</style>
</head>
<body>
  <section class="card card--front">
    <div class="tab tab--top-right"></div>
    <div class="tab tab--bottom-left"></div>
    <div class="wordmark"><span class="wordmark__dot"></span>Corvane Holdings Limited</div>
    <p class="website">www.corvane.bm</p>
  </section>

  <section class="card card--back">
    <div class="tab tab--top-right"></div>
    <div class="tab tab--bottom-left"></div>
    <div class="wordmark"><span class="wordmark__dot"></span>Corvane Holdings Limited</div>

    <div class="person">
      <p class="person__name">Marcus Telford</p>
      <p class="person__role">Director</p>
    </div>

    <ul class="contacts">
      <li>
        <svg viewBox="0 0 28 28" aria-hidden="true"><circle cx="14" cy="14" r="14" fill="var(--teal)"/><path d="M8 12c0-3 12-3 12 0v1.5h-3v-1.5h-6v1.5H8z M9.5 15h9l1.5 5H8z" fill="#fff"/></svg>
        1 441 732 4590
      </li>
      <li>
        <svg viewBox="0 0 28 28" aria-hidden="true"><circle cx="14" cy="14" r="14" fill="var(--teal)"/><rect x="7.5" y="9.5" width="13" height="9" fill="none" stroke="#fff" stroke-width="1.5"/><path d="M7.5 9.5l6.5 5 6.5-5" fill="none" stroke="#fff" stroke-width="1.5"/></svg>
        mtelford@corvane.bm
      </li>
    </ul>

    <div class="company">
      <p class="company__name">Corvane Holdings Limited</p>
      <p class="company__address">P.O. Box KR318, Pemberly KR LT, Bermuda</p>
    </div>
  </section>
</body>
</html>
```